Site Design - PSD Only - festival management

We are looking for a final design for our B2B marketplace. The project is a social commerce platform managing the application and transaction process for festivals and local events. The site design should be based on either Bootstrap or Zurb Foundation. We will provide logos and example images.

Two of the most critical pages will be the home page and the search interface, as well several dashboards. Beyond that, most of the pages will be standard forms and other typical pages that drop into the general site theme. The design tends towards minimalism to simplify the UX and speed up the interface. It incorporates elements from the the following websites. Although the wireframes may lift design elements directly from some of these sites, we are looking for a design that incorporates them more as inspiration.

quilo.co - good example of minimalist structure on internal pages
ravtorn.com - some similarities on search pages, etc.
vexdal.com - nice simple layout for features on home and internal pages
mossbrackle.com - nice alternative to standard bootstrap template

We're nearing the end of this project.  I've received some good submissions , but they are all variations on the exact same theme.  I would still like to see something that doesn't look like a bootstrap template.  I suggested the following idea to a few of the submitters, but now I am adding it to the main project description in hopes of stoking the engine.

The idea I had is for something a little less "bootstrappy" riffs on the design at mossbrackle.com with a flat background color that nicely offsets the blue in the logo. Rather than pulling in a stock image I thought about creating a derivation of the iconic Harrowmere poster, perhaps with vendor tents as tuning pegs and a silhouette of people on the neck. Just throwing that out there. 

I'm not a designer, though, so here's hoping we can see some different ideas while the project is still open.

Thanks.

Target Market(s)

Target market: Festival and event organizers; event participants including exhibitors, vendors, musicians, authors, volunteers, etc.

Industry/Entity Type

Festival

Requirements
Must have
• Home page, Search page, User dash, Organization dash, Event dash, Features, FAQ, various forms
Nice to have
• Would like to see some alternative designs to the standard bootstrap templates...creativity is encouraged.
Should not have
• Should not look like it was pulled off of the shelf.

```html
<!DOCTYPE html>
<html lang="en">
<head>
<meta charset="utf-8">
<title>Festora – Festival &amp; Event Marketplace</title>
<link rel="stylesheet" href="https://fonts.googleapis.com/css2?family=Anton&family=Arimo:wght@400;700&family=Cabin:wght@400;500&family=Ubuntu:wght@500&display=swap">
<style>
  :root {
    --topbar: #222324;
    --blue: #1e86cf;
    --text: #333333;
    --muted: #808080;
    --nav-text: #5a5a5a;
    --line: #dcdcdc;
    --page: #efefef;
    --card: #ffffff;
    --card-head: #f6f6f6;
    --green-top: #6cc21f;
    --green-bottom: #3c9411;
    --yellow: #f4f21a;
  }
  * { margin: 0; padding: 0; box-sizing: border-box; }
  html, body { width: 1200px; height: 882px; overflow: hidden; }
  body { position: relative; background: var(--page); font-family: "Arimo", Arial, sans-serif; color: var(--text); }

  .topbar { position: absolute; left: 0; top: 0; width: 1200px; height: 30px; background: var(--topbar); }
  .btn-small { position: absolute; top: 3px; height: 23px; border-radius: 3px; color: #fff; font: 700 11px "Arimo", sans-serif; display: flex; align-items: center; justify-content: center; }
  .btn-login { left: 186px; width: 50px; background: linear-gradient(#5a5a5a, #3a3a3a); }
  .btn-register { left: 240px; width: 65px; background: linear-gradient(#2c95e0, #1670bd); }
  .social { position: absolute; top: 4px; width: 20px; height: 20px; border-radius: 3px; }
  .social-a { left: 794px; background: #3b5a9a; }
  .social-b { left: 821px; background: #3fb0d8; }
  .social-c { left: 847px; background: #1b7cb4; }
  .search { position: absolute; left: 878px; top: 5px; width: 148px; height: 19px; border-radius: 10px; background: linear-gradient(#3a3a3a, #4a4a4a); }
  .search svg { position: absolute; right: 6px; top: 3px; }

  .header { position: absolute; left: 0; top: 30px; width: 1200px; height: 94px; background: #fff; border-bottom: 1px solid var(--line); }
  .brand { position: absolute; left: 184px; top: 24px; display: flex; align-items: center; gap: 8px; }
  .brand-mark { width: 40px; height: 40px; border-radius: 50%; background: var(--blue); }
  .brand-name { font: 500 39px "Cabin", sans-serif; color: #3a3a3a; letter-spacing: 1px; }
  .quick { position: absolute; top: 0; height: 94px; border-left: 1px solid #e6e6e6; padding: 22px 0 0 23px; }
  .quick:last-child { border-right: 1px solid #e6e6e6; }
  .quick-1 { left: 633px; width: 113px; }
  .quick-2 { left: 746px; width: 135px; }
  .quick-3 { left: 881px; width: 147px; }
  .quick h3 { font: 700 18px "Arimo", sans-serif; color: var(--blue); margin-bottom: 6px; }
  .quick p { font-size: 10.5px; line-height: 12.5px; color: var(--muted); }

  .nav { position: absolute; left: 0; top: 124px; width: 1200px; height: 40px; background: linear-gradient(#ffffff, #e4e4e4); border-bottom: 1px solid #d0d0d0; }
  .nav a { position: absolute; top: 0; height: 40px; display: flex; align-items: center; justify-content: center; font: 700 16px "Arimo", sans-serif; color: var(--nav-text); text-decoration: none; border-right: 1px solid #d6d6d6; }
  .nav a.active { color: var(--blue); }
  .nav .n1 { left: 184px; width: 180px; }
  .nav .n2 { left: 364px; width: 197px; }
  .nav .n3 { left: 561px; width: 156px; }
  .nav .n4 { left: 717px; width: 159px; }
  .nav .n5 { left: 876px; width: 160px; border-right: 0; }

  .hero { position: absolute; left: 0; top: 164px; width: 1200px; height: 397px; overflow: hidden; }
  .hero-photo { position: absolute; inset: 0; background:
      radial-gradient(ellipse 380px 200px at 620px 90px, rgba(206,150,90,.75), transparent 70%),
      radial-gradient(ellipse 260px 200px at 120px 80px, rgba(60,110,200,.6), transparent 70%),
      radial-gradient(ellipse 220px 180px at 1110px 120px, rgba(70,150,210,.55), transparent 70%),
      linear-gradient(#4a3a30 0%, #2a2220 45%, #0e0c0c 100%); }
  .hero h1 { position: absolute; left: 204px; top: 54px; font: 400 72px/76px "Anton", sans-serif; color: #fff; text-transform: uppercase; letter-spacing: 1px; }
  .hero p { position: absolute; left: 206px; top: 216px; width: 520px; font: 400 18px/23px "Cabin", sans-serif; color: #fff; text-transform: uppercase; letter-spacing: -.2px; }
  .cta { position: absolute; left: 206px; top: 289px; width: 247px; height: 60px; border-radius: 4px; background: linear-gradient(var(--green-top), var(--green-bottom)); box-shadow: 0 4px 0 #2c6b0a; display: flex; align-items: center; padding-left: 18px; font: 500 31px "Ubuntu", sans-serif; color: var(--yellow); }
  .cta svg { position: absolute; right: 16px; top: 13px; }
  .slide-arrow { position: absolute; top: 185px; }
  .slide-prev { left: 108px; }
  .slide-next { left: 1064px; }
  .hero-rule { position: absolute; left: 0; top: 561px; width: 1200px; height: 5px; background: #c9c9c9; }

  .feature { position: absolute; top: 589px; width: 263px; height: 300px; background: var(--card); }
  .f1 { left: 192px; } .f2 { left: 474px; } .f3 { left: 755px; }
  .feature-icon { position: absolute; left: 58px; top: 18px; }
  .feature h2 { position: absolute; left: 0; top: 190px; width: 263px; height: 46px; background: var(--card-head); border-top: 1px solid #e2e2e2; border-bottom: 1px solid #e2e2e2; font: 700 16.5px/44px "Arimo", sans-serif; text-align: center; color: #333; }
  .feature h2::before { content: ""; position: absolute; left: 124px; top: -8px; width: 14px; height: 14px; background: var(--card-head); border-left: 1px solid #e2e2e2; border-top: 1px solid #e2e2e2; transform: rotate(45deg); }
  .feature p { position: absolute; left: 26px; top: 251px; width: 211px; font-size: 12.5px; line-height: 16px; text-align: center; color: #777; }
</style>
</head>
<body>

<div class="topbar">
  <div class="btn-small btn-login">Login</div>
  <div class="btn-small btn-register">Register</div>
  <span class="social social-a" aria-hidden="true"></span>
  <span class="social social-b" aria-hidden="true"></span>
  <span class="social social-c" aria-hidden="true"></span>
  <div class="search">
    <svg width="13" height="13" viewBox="0 0 13 13"><circle cx="5" cy="5" r="3.8" fill="none" stroke="#ddd" stroke-width="1.8"/><line x1="7.8" y1="7.8" x2="12" y2="12" stroke="#ddd" stroke-width="2.2"/></svg>
  </div>
</div>

<header class="header">
  <div class="brand"><span class="brand-mark"></span><span class="brand-name">FESTORA</span></div>
  <div class="quick quick-1"><h3>Apply...</h3><p>to a festival or<br>local event</p></div>
  <div class="quick quick-2"><h3>Add...</h3><p>Your event to<br>the Festora network</p></div>
  <div class="quick quick-3"><h3>Join...</h3><p>discussions with<br>industry professionals</p></div>
</header>

<nav class="nav">
  <a class="n1 active" href="#">About Us</a>
  <a class="n2" href="#">Features</a>
  <a class="n3" href="#">FAQ</a>
  <a class="n4" href="#">Blog</a>
  <a class="n5" href="#">Press</a>
</nav>

<section class="hero">
  <div class="hero-photo" role="img" aria-label="Photo of a concert crowd facing a lit stage with performers"></div>
  <h1>Welcome to<br>Festora</h1>
  <p>We connect festival and event organizers with the people that make it happen.</p>
  <div class="cta">Get Started
    <svg width="36" height="36" viewBox="0 0 36 36"><circle cx="18" cy="18" r="17" fill="#1f5f0a"/><path d="M14 10 L26 18 L14 26 Z" fill="#fff"/></svg>
  </div>
  <svg class="slide-arrow slide-prev" width="38" height="38" viewBox="0 0 38 38"><circle cx="19" cy="19" r="17" fill="none" stroke="#fff" stroke-width="2.5"/><path d="M22 11 L14 19 L22 27" fill="none" stroke="#fff" stroke-width="3.5"/></svg>
  <svg class="slide-arrow slide-next" width="38" height="38" viewBox="0 0 38 38"><circle cx="19" cy="19" r="17" fill="none" stroke="#fff" stroke-width="2.5"/><path d="M16 11 L24 19 L16 27" fill="none" stroke="#fff" stroke-width="3.5"/></svg>
</section>
<div class="hero-rule"></div>

<article class="feature f1">
  <svg class="feature-icon" width="148" height="148" viewBox="0 0 148 148">
    <defs>
      <radialGradient id="plate" cx="50%" cy="35%" r="65%"><stop offset="0" stop-color="#fff"/><stop offset="1" stop-color="#e3e3e3"/></radialGradient>
      <linearGradient id="ringBlue" x1="0" y1="0" x2="0" y2="1"><stop offset="0" stop-color="#27b6f0"/><stop offset="1" stop-color="#0a64c8"/></linearGradient>
    </defs>
    <circle cx="74" cy="74" r="73" fill="url(#plate)" stroke="#e4e4e4"/>
    <circle cx="74" cy="74" r="56" fill="url(#ringBlue)"/>
    <circle cx="74" cy="74" r="38" fill="#f7f7f7"/>
    <path d="M60 66 L88 66 L96 80 L96 90 L52 90 L52 80 Z" fill="#555"/>
    <path d="M57 79 L91 79 L86 70 L62 70 Z" fill="#f7f7f7"/>
    <rect x="64" y="80" width="20" height="3" fill="#f7f7f7"/>
  </svg>
  <h2>Online Applications</h2>
  <p>This is a simple hero unit,a simple jumbotron-style component for calling extra attention to featured content.</p>
</article>

<article class="feature f2">
  <svg class="feature-icon" width="148" height="148" viewBox="0 0 148 148">
    <defs>
      <radialGradient id="plate2" cx="50%" cy="35%" r="65%"><stop offset="0" stop-color="#fff"/><stop offset="1" stop-color="#e3e3e3"/></radialGradient>
      <linearGradient id="ringOrange" x1="0" y1="0" x2="0" y2="1"><stop offset="0" stop-color="#f7942e"/><stop offset="1" stop-color="#dc4d0c"/></linearGradient>
    </defs>
    <circle cx="74" cy="74" r="73" fill="url(#plate2)" stroke="#e4e4e4"/>
    <circle cx="74" cy="74" r="56" fill="url(#ringOrange)"/>
    <circle cx="74" cy="74" r="38" fill="#f7f7f7"/>
    <rect x="56" y="58" width="36" height="34" rx="3" fill="#555"/>
    <rect x="62" y="54" width="4" height="8" rx="1" fill="#555"/>
    <rect x="82" y="54" width="4" height="8" rx="1" fill="#555"/>
    <g fill="#f7f7f7">
      <rect x="60" y="67" width="5" height="4"/><rect x="67" y="67" width="5" height="4"/><rect x="74" y="67" width="5" height="4"/><rect x="81" y="67" width="5" height="4"/>
      <rect x="60" y="74" width="5" height="4"/><rect x="67" y="74" width="5" height="4"/><rect x="74" y="74" width="5" height="4"/><rect x="81" y="74" width="5" height="4"/>
      <rect x="60" y="81" width="5" height="4"/><rect x="67" y="81" width="5" height="4"/><rect x="74" y="81" width="5" height="4"/><rect x="81" y="81" width="5" height="4"/>
    </g>
  </svg>
  <h2>Integrated Scheduling</h2>
  <p>This is a simple hero unit,a simple jumbotron-style component for calling extra attention to featured content.</p>
</article>

<article class="feature f3">
  <svg class="feature-icon" width="148" height="148" viewBox="0 0 148 148">
    <defs>
      <radialGradient id="plate3" cx="50%" cy="35%" r="65%"><stop offset="0" stop-color="#fff"/><stop offset="1" stop-color="#e3e3e3"/></radialGradient>
      <linearGradient id="ringPink" x1="0" y1="0" x2="0" y2="1"><stop offset="0" stop-color="#ec3f75"/><stop offset="1" stop-color="#b3003a"/></linearGradient>
    </defs>
    <circle cx="74" cy="74" r="73" fill="url(#plate3)" stroke="#e4e4e4"/>
    <circle cx="74" cy="74" r="56" fill="url(#ringPink)"/>
    <circle cx="74" cy="74" r="38" fill="#f7f7f7"/>
    <rect x="63" y="53" width="22" height="42" rx="4" fill="#555"/>
    <rect x="66" y="59" width="16" height="26" fill="#e6e6e6"/>
    <circle cx="74" cy="90" r="2" fill="#e6e6e6"/>
  </svg>
  <h2>Native Phone and Tablet Apps</h2>
  <p>This is a simple hero unit,a simple jumbotron-style component for calling extra attention to featured content.</p>
</article>

</body>
</html>
```